CD Cover for collection of relaxation music called "Under Quiet Willows"

We'd like to design a CD cover for upload to Brellan Press on Request and to digital services like Tunvo. The template and size specs, photos, example font and text are attached. We need the song durations on the back cover as well and we expect to have those ready by Thursday. Other album and book covers are provided for use as thumbnails inside booklet next to titles. In addition to the finished images to the template specifications, we'd like a copy of the front cover and the back cover as square images to upload to digital services - 2500 dpi x 2500 dpi or larger in .png and .jpg formats. We will also need to add "For more information, visit CalmSoundHarbor.example" under the other available works list. Thanks and we look forward to working together.

Target Market(s)

Relaxation and meditation music. Yoga studios. Massage therapists. Reiki practitioners.

Industry/Entity Type

Music Download

Colors

Designer to choose colors to be used in the design.

Requirements
Must have
• Font consistent with previous works and a peaceful and attractive layout. Also, designers have discretion on which water images to use in which location. The goal is to have a cover image that stands out among other thumbnails in the stores and also for the images on the CD to tell a story of increasing peace and relaxation.

```html
<!DOCTYPE html>
<html lang="en">
<head>
<meta charset="utf-8">
<title>Under Quiet Willows</title>
<link rel="stylesheet" href="https://fonts.googleapis.com/css2?family=Open+Sans:wght@700&display=swap">
<style>
  :root {
    --sky-top: #a9d6e6;
    --sky-mid: #dcedf2;
    --sky-haze: #f4f8f9;
    --sky-horizon: #eef5f6;
    --sea-horizon: #79c0cf;
    --sea-light: #6cb8ca;
    --sea-mid: #56abc0;
    --sea-deep: #2f8fa7;
    --sea-shore: #237f98;
    --title-ink: #004a58;
  }
  html, body {
    margin: 0;
    padding: 0;
    width: 1200px;
    height: 1200px;
    overflow: hidden;
  }
  .cover {
    position: relative;
    width: 1200px;
    height: 1200px;
    overflow: hidden;
  }
  .cover__photo {
    position: absolute;
    inset: 0;
  }
  .cover__sky {
    position: absolute;
    left: 0; top: 0;
    width: 1200px;
    height: 565px;
    background:
      radial-gradient(ellipse 520px 180px at 560px 110px, rgba(255,255,255,0.75), rgba(255,255,255,0) 70%),
      radial-gradient(ellipse 600px 160px at 250px 280px, rgba(255,255,255,0.55), rgba(255,255,255,0) 70%),
      radial-gradient(ellipse 500px 140px at 950px 330px, rgba(255,255,255,0.5), rgba(255,255,255,0) 70%),
      linear-gradient(180deg, var(--sky-top) 0%, var(--sky-mid) 35%, var(--sky-haze) 70%, var(--sky-horizon) 100%);
  }
  .cover__sea {
    position: absolute;
    left: 0; top: 565px;
    width: 1200px;
    height: 635px;
    background:
      radial-gradient(ellipse 700px 120px at 600px 140px, rgba(255,255,255,0.18), rgba(255,255,255,0) 70%),
      linear-gradient(180deg, var(--sea-horizon) 0%, var(--sea-light) 25%, var(--sea-mid) 55%, var(--sea-deep) 82%, var(--sea-shore) 100%);
  }
  .cover__title {
    position: absolute;
    left: 0;
    top: 404px;
    width: 1200px;
    margin: 0;
    text-align: center;
    font-family: "Open Sans", sans-serif;
    font-weight: 700;
    font-size: 124px;
    line-height: 143px;
    color: var(--title-ink);
  }
  .cover__title span { display: block; }
</style>
</head>
<body>
  <main class="cover">
    <div class="cover__photo" role="img" aria-label="Photograph of a calm open sea under a pale cloudy sky, with gentle swells rolling toward the shore">
      <div class="cover__sky"></div>
      <div class="cover__sea"></div>
    </div>
    <h1 class="cover__title">
      <span>Under</span>
      <span>Quiet</span>
      <span>Willows</span>
    </h1>
  </main>
</body>
</html>
```